"Quill Romper" Soil Conditioner for Lawn and Garden.

I need a product label with logo for a square 1 qt F Style plastic Bottle. The area would be 3.75" wide x 4.125" Tall front and back panel. Needs plenty of text area on the back panel.

Target Market(s)

Landscape and Garden

Industry/Entity Type

Home and Garden

Requirements
Must have
• Focus on the problems of heavy soils

```html
<!DOCTYPE html>
<html lang="en">
<head>
<meta charset="utf-8">
<title>Quill Romper Soil Conditioner Label</title>
<link href="https://fonts.googleapis.com/css2?family=Roboto+Condensed:wght@400;700&family=Poppins:wght@600&display=swap" rel="stylesheet">
<style>
  :root {
    --paper: #ffffff;
    --brand-red: #ec1a3b;
    --ink: #1c1c1c;
    --grass: #4f7f2c;
    --soil-light: #6a4327;
    --soil-dark: #4e301b;
    --caution: #f8f250;
    --text-light: #ffffff;
  }
  html, body {
    margin: 0;
    padding: 0;
    width: 1200px;
    height: 911px;
    overflow: hidden;
    background: var(--paper);
  }
  .canvas {
    position: relative;
    width: 1200px;
    height: 911px;
  }
  .label {
    position: absolute;
    left: 170px;
    top: 20px;
    width: 860px;
    height: 870px;
    font-family: "Roboto Condensed", sans-serif;
  }
  .brand {
    position: absolute;
    top: 0;
    left: 0;
    width: 100%;
    height: 350px;
    display: flex;
    flex-direction: column;
    align-items: center;
    justify-content: center;
    gap: 18px;
  }
  .brand-name {
    margin: 0;
    font-family: "Roboto Condensed", sans-serif;
    font-weight: 700;
    font-size: 150px;
    line-height: 0.9;
    text-transform: uppercase;
    text-align: center;
    color: var(--brand-red);
    letter-spacing: -1px;
  }
  .tagline {
    position: absolute;
    top: 352px;
    left: 0;
    width: 100%;
    text-align: center;
    margin: 0;
    font-family: "Poppins", sans-serif;
    font-weight: 600;
    font-size: 35px;
    color: var(--ink);
  }
  .soil-panel {
    position: absolute;
    top: 426px;
    left: 0;
    width: 100%;
    height: 349px;
    background: linear-gradient(to bottom,
      var(--grass) 0%, var(--grass) 12%,
      var(--soil-light) 14%, var(--soil-dark) 100%);
  }
  .product-info {
    position: absolute;
    top: 520px;
    left: 51px;
    width: 700px;
    color: var(--text-light);
  }
  .product-info h2 {
    margin: 0 0 4px;
    font-weight: 700;
    font-size: 34px;
    line-height: 1.2;
  }
  .product-info p {
    margin: 0;
    font-weight: 400;
    font-size: 25.5px;
    line-height: 35px;
  }
  .caution-band {
    position: absolute;
    top: 775px;
    left: 0;
    width: 100%;
    height: 95px;
    background: var(--caution);
    color: var(--ink);
    display: flex;
    align-items: center;
    justify-content: space-between;
    padding: 0 60px 0 58px;
    box-sizing: border-box;
    font-size: 27px;
  }
  .caution strong { font-weight: 700; }
  .net-contents {
    text-align: center;
    line-height: 32px;
    font-size: 26px;
  }
</style>
</head>
<body>
<div class="canvas">
  <section class="label">
    <header class="brand">
      <h1 class="brand-name">Quill<br>Romper</h1>
    </header>
    <p class="tagline">This stuff really works!</p>

    <div class="soil-panel" role="img" aria-label="Illustration of grass on top of a cross-section of brown soil with small stones"></div>

    <div class="product-info">
      <h2>Soil Conditioner for Landscape and Garden:</h2>
      <p>Promotes soil drainage and alleviates puddling and dry spots by opening more pore space for water and air on contact. Lightly apply 1 oz./gal of water with a hose end sprayer, and then water in. Covers 2,500 sq. ft.</p>
    </div>

    <footer class="caution-band">
      <span class="caution"><strong>CAUTION:</strong> Keep out of reach of children!</span>
      <span class="net-contents">Net Contents<br>1 Quart (32 fl.oz.)</span>
    </footer>
  </section>
</div>
</body>
</html>
```